Heron Hotel - Weekly Events Calendar

I run a hotel property in Barbados called the Pelmont (www.thepelmont-stay.example) and we need some flyer templates preparing that we can use weekly on site at the hotel. They need to carry some logo branding but we can keep the balance reasonably informal, however they do need to be able to be edited by our staff easily to fill with the various content each week.
We need three templates, one for our sports bar, one for the music acts we put on in Bar2350 and then one that summarises all the activities each day on site.
I've uploaded a sketch that covers this in more detail.
ideally we use these flyers in a few different ways. We can push them on our app (the Pelmont Resort on the app store), via physical posters and digital posters around site, and on table top paper stands at various outlets.

Keen to see something creative yet simple, and something we can update easily ourselves with content

Target Market(s)

Hotel guests

Colors
0054AA
0677BA
7BADD7
CADEEF
E8F1F8
0094D4
00A9DD
6FCCEA
C7EBF8
E9F6FB

Requirements
Must have
• the ability to be edited each day/week by my team - so likely PPT or word format

```html
<!DOCTYPE html>
<html lang="en">
<head>
<meta charset="utf-8">
<title>The Pelmont – Sports Bar &amp; Live Music Flyers</title>
<link href="https://fonts.googleapis.com/css2?family=Montserrat:wght@500;600;700&family=Titan+One&family=Gelasio:wght@400;500&family=Allura&display=swap" rel="stylesheet">
<style>
  :root{
    --navy:#0054AA;
    --blue:#0677BA;
    --sky:#0094D4;
    --cyan:#00A9DD;
    --light:#6FCCEA;
    --pale:#C7EBF8;
    --mist:#E9F6FB;
    --ink:#1d3b5c;
    --stage:#efebe6;
    --sage:#dde5df;
    --white:#ffffff;
  }
  *{box-sizing:border-box;margin:0;padding:0}
  html,body{width:1200px;height:873px;overflow:hidden;background:var(--stage)}
  .canvas{position:relative;width:1200px;height:873px}

  .flyer{position:absolute;top:66px;width:476px;height:673px;overflow:hidden;box-shadow:0 4px 14px rgba(0,0,0,.12)}
  .flyer--sports{left:92px;background:linear-gradient(180deg,#e2e9e3 0%,var(--sage) 70%,#e8eeea 100%)}
  .flyer--music{left:616px;background:var(--white)}

  .brand{position:absolute;top:22px;left:0;width:100%;text-align:center}
  .brand__name{font-family:"Montserrat",sans-serif;font-weight:600;font-size:30px;color:var(--blue);letter-spacing:.5px;line-height:1}
  .brand__tag{margin-top:10px;font-family:"Montserrat",sans-serif;font-weight:500;font-size:10px;letter-spacing:2px;color:var(--blue)}

  /* Sports flyer */
  .headline{position:absolute;left:0;width:100%;text-align:center;font-family:"Titan One",sans-serif;color:var(--cyan);text-shadow:4px 4px 0 var(--white);line-height:1}
  .headline--sports{top:88px;font-size:74px;letter-spacing:1px}
  .headline--bar{top:166px;font-size:72px;color:var(--sky)}

  .athlete{position:absolute;left:276px;top:214px;width:190px;height:426px;border-radius:40% 40% 10% 10%;background:radial-gradient(ellipse at 50% 45%,#8a6a55 0%,#4a3b35 45%,rgba(221,229,223,0) 75%)}

  .fixture{position:absolute;left:40px;width:211px;height:100px;background:var(--white);clip-path:polygon(0 0,100% 0,82% 100%,0 100%);font-family:"Montserrat",sans-serif;color:var(--blue)}
  .fixture--dark{background:var(--blue);color:var(--white)}
  .fixture__sport{position:absolute;left:24px;top:15px;font-weight:700;font-size:14.5px;letter-spacing:.3px}
  .fixture__teams{position:absolute;left:24px;top:41px;font-size:9.5px;font-weight:500;display:flex;align-items:center;gap:10px}
  .fixture__vs{font-size:15px;font-weight:600;color:var(--light)}
  .fixture__date{position:absolute;left:0;top:66px;width:149px;height:18px;background:var(--cyan);color:var(--white);font-size:9.5px;font-weight:500;line-height:18px;padding-left:24px}

  .splash{position:absolute;left:0;bottom:0;width:100%;height:110px;background:linear-gradient(180deg,rgba(255,255,255,0) 0%,rgba(255,255,255,.85) 40%,var(--white) 70%)}

  .contact{position:absolute;left:0;bottom:12px;width:100%;display:flex;justify-content:center;gap:22px;font-family:"Montserrat",sans-serif;font-size:6px;font-weight:600;color:#222}
  .contact__item{display:flex;align-items:center;gap:5px}
  .contact__icon{width:15px;height:15px;border-radius:50%;background:var(--cyan);display:flex;align-items:center;justify-content:center}

  /* Music flyer */
  .stage-art{position:absolute;left:0;top:70px;width:100%;height:603px;background:
      radial-gradient(ellipse at 15% 5%,#3b2f8f 0%,rgba(59,47,143,0) 35%),
      radial-gradient(ellipse at 95% 10%,#b86a3c 0%,rgba(184,106,60,0) 30%),
      radial-gradient(ellipse at 60% 30%,#8a3fb0 0%,rgba(138,63,176,0) 35%),
      linear-gradient(180deg,#dfe6ee 15%,#8898aa 40%,#2b3a4e 62%,#1b4f80 85%,#0c4a86 100%)}
  .stage-art__guitar{position:absolute;left:20px;top:515px;width:436px;height:158px;border-radius:50% 50% 0 0/40% 40% 0 0;background:linear-gradient(180deg,#d3a56a 0%,#a77c48 45%,rgba(12,74,134,.6) 100%)}
  .header-curve{position:absolute;left:0;top:60px;width:476px;height:40px}

  .lineup{position:absolute;left:44px;top:99px;display:grid;grid-template-columns:184px 184px;grid-auto-rows:111px;column-gap:20px;row-gap:18px}
  .act{background:var(--white);text-align:center;position:relative}
  .act__date{position:absolute;top:8px;left:0;width:100%;font-family:"Allura",cursive;font-size:19px;color:#222}
  .act__name{position:absolute;top:36px;left:0;width:100%;font-family:"Gelasio",serif;font-size:18.5px;color:#1a5587}
  .act__time{position:absolute;top:68px;left:36px;width:112px;height:30px;background:var(--cyan);border:1.5px solid var(--cyan);box-shadow:inset 0 0 0 1.5px var(--white);font-family:"Gelasio",serif;font-size:9.5px;color:var(--white);line-height:27px}

  .venue{position:absolute;right:22px;bottom:18px;font-family:"Gelasio",serif;font-size:20px;color:var(--white)}
</style>
</head>
<body>
<main class="canvas">

  <section class="flyer flyer--sports">
    <header class="brand">
      <div class="brand__name">The Pelmont</div>
      <div class="brand__tag">SINCE 1923 • BARBADOS</div>
    </header>

    <div class="athlete" role="img" aria-label="Photo of a sprinter in black sportswear in a running start pose"></div>

    <h1 class="headline headline--sports">SPORTS</h1>
    <h1 class="headline headline--bar">BAR</h1>

    <article class="fixture" style="top:251px">
      <div class="fixture__sport">FOOTBALL</div>
      <div class="fixture__teams"><span>TEAM A</span><span class="fixture__vs">(VS)</span><span>TEAM B</span></div>
      <div class="fixture__date">MAY 20 MONDAY - 12PM</div>
    </article>
    <article class="fixture fixture--dark" style="top:363px">
      <div class="fixture__sport">TENNIS</div>
      <div class="fixture__teams"><span>TEAM A</span><span class="fixture__vs">(VS)</span><span>TEAM B</span></div>
      <div class="fixture__date">MAY 20 MONDAY - 12PM</div>
    </article>
    <article class="fixture" style="top:474px">
      <div class="fixture__sport">FOOTBALL</div>
      <div class="fixture__teams"><span>TEAM A</span><span class="fixture__vs">(VS)</span><span>TEAM B</span></div>
      <div class="fixture__date">MAY 20 MONDAY - 12PM</div>
    </article>

    <div class="splash"></div>

    <footer class="contact">
      <span class="contact__item"><span class="contact__icon"><svg width="8" height="8" viewBox="0 0 24 24"><path fill="#fff" d="M6.6 10.8a15 15 0 0 0 6.6 6.6l2.2-2.2a1 1 0 0 1 1-.25 11.4 11.4 0 0 0 3.6.57 1 1 0 0 1 1 1V20a1 1 0 0 1-1 1A17 17 0 0 1 3 4a1 1 0 0 1 1-1h3.5a1 1 0 0 1 1 1c0 1.25.2 2.45.57 3.57a1 1 0 0 1-.25 1z"/></svg></span>(246) 555-0148</span>
      <span class="contact__item"><span class="contact__icon"><svg width="8" height="8" viewBox="0 0 24 24"><path fill="#fff" d="M3 5h18v14H3z"/><path fill="none" stroke="#00A9DD" stroke-width="2" d="M3 6l9 7 9-7"/></svg></span>stay@thepelmont-stay.example</span>
      <span class="contact__item"><span class="contact__icon"><svg width="8" height="8" viewBox="0 0 24 24"><path fill="#fff" d="M12 2a7 7 0 0 0-7 7c0 5 7 13 7 13s7-8 7-13a7 7 0 0 0-7-7zm0 9.5A2.5 2.5 0 1 1 12 6.5a2.5 2.5 0 0 1 0 5z"/></svg></span>St. Lucy, Barbados - BB26051</span>
    </footer>
  </section>

  <section class="flyer flyer--music">
    <div class="stage-art" role="img" aria-label="Flowing purple and orange music-note ribbon over a dark stage, with an acoustic guitar at the bottom">
      <div class="stage-art__guitar"></div>
    </div>
    <svg class="header-curve" viewBox="0 0 476 40" preserveAspectRatio="none" aria-hidden="true"><path fill="#fff" d="M0 0H476V10C380 40 300 10 240 18 160 28 80 30 0 10Z"/></svg>

    <header class="brand">
      <div class="brand__name">The Pelmont</div>
      <div class="brand__tag">SINCE 1923 • BARBADOS</div>
    </header>

    <div class="lineup">
      <article class="act"><div class="act__date">Tuesday 12 May</div><div class="act__name">Darvel Quinn</div><div class="act__time">Live Form 7.00Pm</div></article>
      <article class="act"><div class="act__date">Tuesday 12 May</div><div class="act__name">Marisse</div><div class="act__time">Live Form 7.00Pm</div></article>
      <article class="act"><div class="act__date">Tuesday 12 May</div><div class="act__name">Tobiah</div><div class="act__time">Live Form 7.00Pm</div></article>
      <article class="act"><div class="act__date">Tuesday 12 May</div><div class="act__name">Solenne</div><div class="act__time">Live Form 7.00Pm</div></article>
      <article class="act"><div class="act__date">Tuesday 12 May</div><div class="act__name">Kiran</div><div class="act__time">Live Form 7.00Pm</div></article>
      <article class="act"><div class="act__date">Tuesday 12 May</div><div class="act__name">John Doe</div><div class="act__time">Live Form 7.00Pm</div></article>
    </div>

    <div class="venue">Bar2350</div>
  </section>

</main>
</body>
</html>
```